Pelham Design & Millwork needs a web presence. Looking for a unique Design so please submit an idea.

In brief, you should know the following about me: My company was established in 2001 and had been responsible for providing reasonable CAD Design and Custom Millwork ever since. My specialty is in the area Architectural CAD Design, Fabrication of Custom Millwork and Mouldings on a partime basis. Drawings and estimates done at a very reasonable cost. I look forward to working on your next project. Thanks in Advance, Boyd 
I would like one page to show thumbnails linked to some of past millwork projects and another page with thumbnails linking to some of my house designs. I assume last page will have contact information accessed from a link on home page. I already had a logo designed which I can supply you with to design home page around. As I indicated I have a regular full time job and do this for additional income and will move to full time when I have enough business.

I have attached the logo I had designed in a couple different colors. I have also uploaded some PDF's of files that I also considered before choosing the RED LOGO to give an ideas of how we could tweak the logo to better fit the website if need be. Text is wrong in those.

Thanks,
Boyd

I added my logo as a PDF side there seems to be a problem with scaling loge with the other file. Hope this helps.

Boyd

Evening,
I will be hosting this site on wavecrib. Its looks like it will get launched with wordpress?  What will be involved from getting your design up so I can upload project pictures and and text to areas you have set aside? I am also going to upload a couple jpg of a couple recent projects so you can put in so I can get a feel of what they will look like. Thanks for all your work to date! Boyd

I am not seeing alot of design variations or even many designers in fact. Is there something more from me you need? Do you need me to extend deadline?

Reason: It appears that your need some more time to submit some design changes. I will choose a design next week after changes have been submitted. Thanks for your time. Boyd

Reason: Designers needs a couple days to submit some last minute changes. Thanks for all your submissions! Boyd

Reason: Some last minute designs that I need to look at and give feedback on. I want to thank everyone for their designs and patience. Thanks again, Boyd

Evening All,

Upon discussion with a couple of the designers I want the design done in Word Press and I have increased budget the amount they said they would need to do it for. Thanks for all submissions so far but I am still looking for the special one that stands out among the rest! Boyd

I will not be extending deadline and choosing designer tomorrow morning so if you have anything else to add please do so tonight. Thanks for all your submissions. Boyd

Target Market(s)

Millwork projects will be generally local where as CAD Design Projects could be emailed anywhere. Probably more USA but who knows.

Industry/Entity Type

House

Font styles to use
Other font styles liked:
• Eras Medium ITC, Calibri or Designers choice.

Requirements
Must have
• Must tie in my logo on Homepage at least. Could even be somewhat transparent in background? I will let the designer work that out.
Nice to have
• Page to point to current and past Design projects on one page and millwork on another.
Should not have
• Target a large Corporate or Global environment since it is a small business right now.

```html
<!DOCTYPE html>
<html lang="en">
<head>
<meta charset="utf-8">
<title>Pelham Design &amp; Millwork</title>
<link href="https://fonts.googleapis.com/css2?family=Open+Sans:wght@400;600&family=Varela+Round&display=swap" rel="stylesheet">
<style>
:root{
  --brand-red:#9b1c1f;
  --band-top:#a3302f;
  --band-bottom:#6a0e12;
  --ink:#333;
  --muted:#888;
  --rule:#e3e3e3;
  --footer:#363636;
  --white:#fff;
}
*{margin:0;padding:0;box-sizing:border-box}
html,body{width:926px;height:1200px;overflow:hidden;background:var(--white)}
body{position:relative;font-family:'Open Sans',sans-serif;color:var(--ink)}
.abs{position:absolute}
.heading{font-family:'Varela Round',sans-serif;font-weight:400}

/* header */
.brand{left:58px;top:28px;display:flex;align-items:center;gap:8px}
.brand-mark{width:22px;height:22px;background:var(--brand-red)}
.brand-name{font-size:19px;font-weight:600;color:var(--brand-red);line-height:1.1}
.brand-name small{display:block;font-size:19px}
.call{right:72px;top:30px;text-align:right}
.call-label{font-size:12px;color:#555;letter-spacing:.2px}
.call-number{font-size:22px;color:var(--brand-red);line-height:1.2}
.main-nav{right:72px;top:86px;display:flex;font-size:13.5px;font-weight:600;text-transform:uppercase}
.main-nav a{color:var(--ink);text-decoration:none;padding:0 15px;border-left:1px solid #bbb;line-height:14px}
.main-nav a:first-child{border-left:0}
.main-nav a:last-child{padding-right:0}
.main-nav a.current{color:var(--brand-red)}

/* hero */
.hero{left:0;top:125px;width:926px;height:376px;
  background:radial-gradient(ellipse at 60% 55%,#7fa6c9 0%,#35577a 30%,#1d3244 60%,#14241c 100%)}
.hero-title{left:67px;top:220px;color:var(--white);font-size:27px;line-height:1.2}
.hero-sub{left:67px;top:257px;color:var(--white);font-size:21px;line-height:31px}
.hero-text{left:68px;top:321px;color:#e8e8e8;font-size:10px;line-height:16px;width:240px}
.dots{left:69px;top:364px;display:flex;gap:5px}
.dots span{width:11px;height:11px;border-radius:50%;background:rgba(255,255,255,.3)}
.dots span:first-child{background:var(--white)}

/* red band */
.features{left:0;top:501px;width:926px;height:164px;background:linear-gradient(var(--band-top),var(--band-bottom))}
.feature{color:var(--white)}
.feature h2{font-family:'Varela Round',sans-serif;font-weight:400}
.feature p{color:#e6c2c2;font-size:10.5px;line-height:18.5px}
.f1{left:80px;top:527px;width:255px}
.f1 h2{font-size:24px;margin-bottom:4px}
.f1 p{margin-left:2px}
.f2{left:398px;top:533px;width:210px}
.f2 h2{font-size:19px;line-height:24px;margin-bottom:5px}
.f2 p{font-size:10px;line-height:16px}
.f3{left:655px;top:541px;width:210px}
.f3 h2{font-size:19px;margin-bottom:4px}
.f3 p{font-size:10px;line-height:16px}
.dividers{left:0;top:501px}

/* intro */
.intro{left:0;top:705px;width:926px;text-align:center}
.intro h1{font-family:'Varela Round',sans-serif;font-weight:400;font-size:24px;line-height:32px}
.intro p{font-size:16.5px;color:#444;margin-top:2px}

/* services */
.section-title{font-family:'Varela Round',sans-serif;font-weight:400;color:var(--brand-red);font-size:20px}
.services{left:70px;top:826px;width:192px}
.services ul{list-style:none;margin-top:8px}
.services li{font-size:11.5px;height:27px;line-height:27px;border-bottom:1px solid #ececec;padding-left:15px;position:relative}
.services li:last-child{border-bottom:0}
.services li::before{content:"";position:absolute;left:2px;top:10px;border-left:5px solid #bbb;border-top:4px solid transparent;border-bottom:4px solid transparent}

/* blogs */
.blogs{left:293px;top:826px;width:280px}
.post{position:absolute;left:1px;width:280px;height:52px}
.post-thumb{position:absolute;left:0;top:0;width:64px;height:50px}
.post-title{position:absolute;left:75px;top:-1px;font-size:11.5px;font-weight:600;color:#444}
.post-text{position:absolute;left:75px;top:17px;font-size:9px;color:var(--muted);line-height:14px;width:200px}

/* projects */
.projects{left:585px;top:813px;width:278px;height:234px;border:1px solid #d6d6d6;background:#f4f4f4}
.projects h3{position:absolute;left:17px;top:14px;font-family:'Open Sans',sans-serif;font-weight:400;font-size:19px;color:#444}
.tile{position:absolute;width:76px;height:75px;background:var(--white);padding:4px;box-shadow:0 1px 2px rgba(0,0,0,.18)}
.tile div{width:100%;height:100%}

/* footer */
.footer-edge{left:0;top:1093px;width:926px;height:7px;background:repeating-linear-gradient(135deg,#e4e4e4 0 2px,#f6f6f6 2px 4px)}
.footer{left:0;top:1100px;width:926px;height:100px;background:var(--footer)}
.footer-nav{left:68px;top:1125px;display:flex;font-size:12.5px;color:#ddd}
.footer-nav a{color:#ddd;text-decoration:none;padding:0 8px;border-left:1px solid #999;line-height:13px}
.footer-nav a:first-child{padding-left:0;border-left:0}
.copyright{left:68px;top:1151px;font-size:10.5px;color:#8a8a8a}
.social{left:758px;top:1128px;display:flex;gap:8px}
.social span{width:19px;height:19px;border-radius:2px}
</style>
</head>
<body>

<header>
  <div class="abs brand">
    <span class="brand-mark"></span>
    <div class="brand-name">Pelham<small>Design &amp; Millwork</small></div>
  </div>
  <div class="abs call">
    <div class="call-label">CALL US NOW</div>
    <div class="call-number">555-284-0193</div>
  </div>
  <nav class="abs main-nav">
    <a class="current" href="#">Home</a>
    <a href="#">About us</a>
    <a href="#">Millwork projects</a>
    <a href="#">House designs</a>
    <a href="#">Contact us</a>
  </nav>
</header>

<section>
  <div class="abs hero" role="img" aria-label="Night rendering of a modern curved museum building with palm trees and lit plaza"></div>
  <h1 class="abs heading hero-title">Architectural CAD Design</h1>
  <p class="abs heading hero-sub">and Fabrication Custom<br>Millwork and Mouldings.</p>
  <p class="abs hero-text">Aliquam nec erat at purus cursus interdum Vestibu-lum ligula augue bibendum accumsan vestibulum</p>
  <div class="abs dots"><span></span><span></span><span></span><span></span></div>
</section>

<section>
  <div class="abs features"></div>
  <svg class="abs dividers" width="926" height="164" viewBox="0 0 926 164" aria-hidden="true">
    <line x1="389" y1="18" x2="331" y2="150" stroke="rgba(255,255,255,.35)" stroke-width="1"/>
    <line x1="649" y1="18" x2="591" y2="150" stroke="rgba(255,255,255,.35)" stroke-width="1"/>
  </svg>
  <div class="abs feature f1">
    <h2>Why Choose Us</h2>
    <p>Aliquam nec erat at purus cursus interdum Vestibu-lum ligula augue bibendum accumsan vestibulum ut commodo a mi Morbi ornare gravida elit Integer congue augue et malesuada iaculis</p>
  </div>
  <div class="abs feature f2">
    <h2>Best Architectural<br>CAD Design</h2>
    <p>Consectetuer mi, a ultricies massa est sed nisl. Class aptent taciti sociosqu ad litora torquent per conubia nostra</p>
  </div>
  <div class="abs feature f3">
    <h2>Want Hire Us Now</h2>
    <p>Consectetuer mi, a ultricies massa est sed nisl. Class aptent taciti sociosqu ad litora torquent per conubia nostra</p>
  </div>
</section>

<section class="abs intro">
  <h1>Pellentesque faucibus Ut accumsan ultricies elit</h1>
  <p>Mauris nunc quam venenatis nec euismod sit amet&nbsp; egestas placerat est Pellentesque habitant</p>
</section>

<section class="abs services">
  <h2 class="section-title">Services We Provide</h2>
  <ul>
    <li>Vivamus porttitor purus</li>
    <li>Nisi eleifend libero a tempus</li>
    <li>Libero lectus feugiat</li>
    <li>Morbi diam mauris</li>
    <li>Viverra in gravida</li>
    <li>Libero lectus feugiat</li>
  </ul>
</section>

<section class="abs blogs">
  <h2 class="section-title">Latest Blogs</h2>
  <article class="post" style="top:34px">
    <div class="post-thumb" role="img" aria-label="Warm lit restaurant interior with curved wood walls" style="background:linear-gradient(135deg,#d9b98a,#8a6a45)"></div>
    <div class="post-title">Etiam est nunc venenatis</div>
    <div class="post-text">Class aptent taciti sociosqu ad litora torquent per conubia nostra, per inceptos</div>
  </article>
  <article class="post" style="top:98px">
    <div class="post-thumb" role="img" aria-label="Modern building facade lit in blue and purple at night" style="background:linear-gradient(135deg,#3a3c8a,#b7b9d8)"></div>
    <div class="post-title">Mauris neque metus</div>
    <div class="post-text">Class aptent taciti sociosqu ad litora torquent per conubia nostra hymenaeos</div>
  </article>
  <article class="post" style="top:162px">
    <div class="post-thumb" role="img" aria-label="Contemporary house with wood slat and stone facade" style="background:linear-gradient(135deg,#c9c3b6,#6b5a45)"></div>
    <div class="post-title">Curabitur iaculis</div>
    <div class="post-text">Class aptent taciti sociosqu per conubia nostra, per inceptos hymenaeos</div>
  </article>
</section>

<section class="abs projects">
  <h3>Recent Projects</h3>
  <a class="tile" style="left:15px;top:48px"><div role="img" aria-label="Dark modern townhouse exterior" style="background:linear-gradient(#b8c6d6,#5a4a3c)"></div></a>
  <a class="tile" style="left:104px;top:48px"><div role="img" aria-label="White modern house with wood overhang" style="background:linear-gradient(#7fa9d4,#d8d2c8)"></div></a>
  <a class="tile" style="left:190px;top:48px"><div role="img" aria-label="White terraced house with greenery" style="background:linear-gradient(#dfe6e4,#93a58a)"></div></a>
  <a class="tile" style="left:15px;top:134px"><div role="img" aria-label="Three storey house with balconies" style="background:linear-gradient(#a9c0d4,#5c5448)"></div></a>
  <a class="tile" style="left:104px;top:134px"><div role="img" aria-label="Modern house with orange panels" style="background:linear-gradient(#6d95c2,#b86b3e)"></div></a>
  <a class="tile" style="left:190px;top:134px"><div role="img" aria-label="Orange timber clad house at dusk" style="background:linear-gradient(#4c7fb8,#c0542a)"></div></a>
</section>

<footer>
  <div class="abs footer-edge"></div>
  <div class="abs footer"></div>
  <nav class="abs footer-nav">
    <a href="#">Home</a>
    <a href="#">About us</a>
    <a href="#">Millwork projects</a>
    <a href="#">House designs</a>
    <a href="#">Contact us</a>
  </nav>
  <p class="abs copyright">Copyright © 2013 Company Name.&nbsp; All right reseved</p>
  <div class="abs social" aria-label="Social links">
    <span style="background:#3b5a9a"></span>
    <span style="background:#3fb1e0"></span>
    <span style="background:#1a78b4"></span>
    <span style="background:#f08a1c"></span>
  </div>
</footer>

</body>
</html>
```